Pinewell Enterprise Forge Website Redesign

Objective: The primary goal of the website redesign is to effectively communicate with Small Business Owners, offering them custom business advisory services to drive growth. The redesigned website should be interactive, easy to read, and feature clear calls to action.

PEF provides custom business advisory services tailored to small enterprises, focusing on driving growth through a comprehensive 3-step process; Diagnostic, Remedial and Strategic roadmap development

1. Diagnostic Assessment:
a. In-depth analysis to identify business strengths, weaknesses, and opportunities.
b. Comprehensive evaluation to understand the unique needs of each small enterprise.
2. Remedial Care:
a. Implementation of tailored solutions to address identified issues.
b. Hands-on support to navigate challenges and obstacles.
3. Roadmap to Growth:
a. Development of a strategic roadmap outlining actionable steps for sustainable growth.
b. Ongoing guidance and support to ensure successful execution.

The Unique Selling Proposition (USP): PEF stands out by:
• Handholding businesses through their growth journey.
• Providing a clear roadmap to sustainable growth.
• Leveraging a network of industry experts for specialized advice.
Target Customers: PEF caters to the following target customers:
• Start-ups seeking to launch successfully.
• Businesses looking to achieve substantial growth.
• Entrepreneurial enterprises seeking support.
• Mature businesses facing distress and seeking turnaround strategies.
Services Offered:
1. Bespoke Packages:
a. Tailored advisory services to meet the unique needs of each client.
b. Personalized solutions for businesses at different stages of growth.
2. Training, Mentorship, and Coaching:
a. Skill-building programs for business owners and key staff.
b. Ongoing mentorship and coaching to foster continuous improvement.
3. Incubation:
a. Support for start-ups with physical and virtual resources.
b. Incubation programs to nurture and guide emerging businesses.
4. Specialized Programs:
a. Women Entrepreneurs:
b. Tailored programs to support and empower women in business.
c. Youth Entrepreneurs: Initiatives to cultivate and guide young entrepreneurs.

Design Preferences:
• Layout flow to tell the brand story
• Interactive design elements
• Easy-to-read and understand content.
• Clear and prominent calls to action.
Key Messages:
• Expert Business Advisory for Small Enterprises.
• Your Partner in Growth – from Assessment to Execution.
• Join a Network of Successful Entrepreneurs.
Brand Guidelines:
• Use the existing brand colors and logo.
• Maintain a professional and approachable tone throughout the website.
Deliverables:
• Responsive website design for desktop and mobile.
• Mockups for key pages.
• Clear navigation structure for easy user experience.
• Integration of interactive elements.

Similar Businesses
https://ventrahelpers.co.uk/free-resources/
https://www.calderwick.ac.uk/business-services/engage-with-us/talent-and-insight/the-venture-yard/
https://www.foundersloft.ng/the-venture-yard/
https://theventureyard.io/

Design ad Layout Inspiration
https://trouvemirelle.com/en/
https://www.qx.com/en_gl/big-data-analytics

Target Market(s)

PEF caters to the following target customers: • Start-ups seeking to launch successfully. • Businesses looking to achieve substantial growth. • Entrepreneurial enterprises seeking support. • Mature businesses facing distress and seeking turnaround strategies.

Industry/Entity Type

Business Consulting and Advisory

Number of Pages Required

3 page

Requirements
Must have
• • Clear and prominent calls to action.
Nice to have
• • Interactive design elements. • Easy-to-read and understand content.

```html
<!DOCTYPE html>
<html lang="en">
<head>
<meta charset="utf-8">
<title>PEF — About Us</title>
<link href="https://fonts.googleapis.com/css2?family=Lato:wght@700;900&family=Roboto:wght@400;500;700&display=swap" rel="stylesheet">
<style>
:root{
  --navy:#0b2f66;
  --blue:#1a6fa3;
  --cyan:#3fc6e6;
  --text:#555b66;
  --dark:#1a1f2b;
  --white:#ffffff;
}
*{margin:0;padding:0;box-sizing:border-box}
html,body{width:1200px;height:3126px;overflow:hidden;background:var(--white)}
body{position:relative;font-family:'Roboto',sans-serif;color:var(--text)}
.abs{position:absolute}

/* header */
.site-header{position:absolute;left:0;top:0;width:1200px;height:138px;background:var(--white);z-index:3}
.brand{position:absolute;left:112px;top:40px;font:700 54px/1 'Lato',sans-serif;color:var(--navy);letter-spacing:-1px}
.main-nav{position:absolute;top:63px;left:0;font:500 14px/1 'Roboto',sans-serif;color:var(--dark);text-transform:uppercase}
.main-nav a{position:absolute;white-space:nowrap;color:inherit;text-decoration:none}
.main-nav a.is-active{color:var(--cyan)}
.btn{position:absolute;display:flex;align-items:center;justify-content:center;font:700 14px/1 'Roboto',sans-serif;color:var(--white);text-transform:uppercase;background:linear-gradient(90deg,var(--navy),var(--cyan))}
.btn::after{content:"";position:absolute;left:7px;top:7px;right:-7px;bottom:-7px;border:1px solid #9aa8bd;z-index:-1}
.btn-contact{left:946px;top:44px;width:135px;height:47px;z-index:1}

/* hero */
.hero{position:absolute;left:0;top:138px;width:1200px;height:600px}
.hero-photo{position:absolute;inset:0;background:linear-gradient(90deg,#8b7a6e 0%,#c9c3bd 22%,#ecebea 45%,#f4f4f4 70%,#ececec 100%)}
.hero-title{position:absolute;left:0;width:1200px;top:198px;text-align:center;font:900 58px/1 'Lato',sans-serif;color:var(--navy)}

/* about */
.section-title{font:900 41px/1 'Lato',sans-serif;color:var(--navy)}
.section-title span{color:var(--cyan)}
.about-title{position:absolute;left:112px;top:816px}
.about-copy{position:absolute;left:112px;top:880px;width:413px}
.about-copy p,.about-long p{font-size:16px;line-height:26.6px;text-align:justify;margin-bottom:14px}
.about-photo{position:absolute;left:597px;top:819px;width:489px;height:428px;background:linear-gradient(120deg,#7a5a3e 0%,#b08a63 35%,#d8cfc6 60%,#2b3550 100%);z-index:1}
.dot-grid{position:absolute;left:564px;top:1126px;width:160px;height:160px}
.about-long{position:absolute;left:112px;top:1324px;width:976px}

/* contact */
.marble{position:absolute;left:0;top:1980px;width:1200px;height:820px;background:linear-gradient(160deg,#eef0f2 0%,#fafafa 30%,#e7e9ec 55%,#f7f7f8 80%,#eceef0 100%)}
.contact-title{position:absolute;left:0;width:1200px;top:2256px;text-align:center;font-size:44px}
.field{position:absolute;background:var(--white);border:1px solid #e4e6ea;box-shadow:0 2px 8px rgba(0,0,0,.05);font-size:14px;color:#777;padding:17px 17px}
.btn-send{left:520px;top:2511px;width:152px;height:49px;z-index:1}

/* footer */
.footer-text{color:var(--white)}
.footer-brand{position:absolute;left:112px;top:2896px;width:200px;font:700 24px/1.15 'Roboto',sans-serif;color:var(--white)}
.col-rule{position:absolute;width:2px;background:rgba(255,255,255,.85);top:2785px;height:22px}
.col-line{position:absolute;width:1px;background:rgba(255,255,255,.35);top:2807px;height:251px}
.col-title{position:absolute;top:2809px;font:500 17px/1 'Roboto',sans-serif;color:var(--white);text-transform:uppercase}
.quick-links{position:absolute;left:368px;top:2849px;list-style:none}
.quick-links li{height:32.7px;font-size:14px;color:var(--white);display:flex;align-items:center;gap:14px}
.info-item{position:absolute;left:553px;color:var(--white)}
.info-item svg{position:absolute;left:0;top:1px}
.info-item h4{position:absolute;left:33px;top:0;font:500 14px/1 'Roboto',sans-serif;white-space:nowrap}
.info-item p{position:absolute;left:33px;top:21px;font-size:11.5px;line-height:19px;width:170px}
.news-input{position:absolute;left:809px;top:2851px;width:283px;height:49px;background:var(--white);font-size:13px;color:#555;padding:17px 18px}
.social{position:absolute;top:2921px;width:38px;height:38px;border-radius:50%;border:1.5px solid var(--white)}
.footer-rule{position:absolute;left:115px;top:3058px;width:977px;height:1px;background:rgba(255,255,255,.4)}
.copyright{position:absolute;left:0;width:1200px;top:3084px;text-align:center;font-size:12px;color:var(--white)}
</style>
</head>
<body>

<header class="site-header">
  <div class="brand">PEF</div>
  <nav class="main-nav">
    <a style="left:437px">Home</a>
    <a class="is-active" style="left:511px">About Us</a>
    <a style="left:613px">Services <svg width="10" height="7" viewBox="0 0 10 7" style="margin-left:4px"><path d="M1 1l4 4 4-4" fill="none" stroke="#1a1f2b" stroke-width="1.5"/></svg></a>
    <a style="left:728px">Our Process</a>
    <a style="left:859px">Blog</a>
  </nav>
  <a class="btn btn-contact">Contact Us</a>
</header>

<section class="hero">
  <div class="hero-photo" role="img" aria-label="Businesswoman smiling on a phone call at her laptop in a bright office"></div>
  <h1 class="hero-title">ABOUT US</h1>
</section>

<svg class="abs" style="left:0;top:500px;z-index:2" width="1200" height="250" viewBox="0 500 1200 250">
  <defs>
    <linearGradient id="vee" x1="0" x2="1">
      <stop offset="0" stop-color="#0b3f7a"/><stop offset="1" stop-color="#35b3d8"/>
    </linearGradient>
  </defs>
  <path d="M0 522 L400 710 L1200 534 L1200 750 L0 750Z" fill="#fff"/>
  <path d="M158 607 L400 734 L880 613 L400 708Z" fill="url(#vee)"/>
</svg>

<h2 class="section-title about-title">ABOUT <span>US</span></h2>
<div class="about-copy">
  <p>Lorem ipsum dolor sit amet, consectetur adipiscing elit, sed do eiusmod tempor incididunt ut labore et dolore magna aliqua. Ut enim ad minim veniam, quis nostrud exercitation ullamco nisi ut aliquip exea.</p>
  <p>Lorem ipsum dolor sit amet, consectetur adipiscing elit, sed do eiusmod tempor incididunt ut labore et dolore magna aliqua ut enim ad minim veniam.</p>
  <p>Lorem ipsum dolor sit amet, consectetur adipiscing elit, sed do eiusmod tempor incididunt ut labore et dolore magna aliqua. Ut enim ad minim veniam, quis nostrud exercitation ullamco nisi ut aliquip exea.</p>
  <p>Lorem ipsum dolor sit amet, consectetur adipiscing elit, sed do eiusmod tempor incididunt ut labore et dolore magna aliqua ut enim ad minim veniam.</p>
</div>
<svg class="dot-grid" viewBox="0 0 160 160" aria-hidden="true">
  <defs><pattern id="dots" width="11" height="11" patternUnits="userSpaceOnUse"><circle cx="2" cy="2" r="1.1" fill="#4a5568"/></pattern></defs>
  <rect width="160" height="160" fill="url(#dots)"/>
</svg>
<div class="about-photo" role="img" aria-label="Smiling businesswoman in a navy blazer seated at a desk with a laptop"></div>

<div class="about-long">
  <p>Lorem ipsum dolor sit amet, consectetur adipiscing elit, sed do eiusmod tempor incididunt ut labore et dolore magna aliqua. Ut enim ad minim veniam, quis nostrud exercitation ullamco laboris nisi ut aliquip ex ea commodo consequat. Duis aute irure dolor in reprehenderit in voluptate velit esse cillum dolore eu fugiat nulla pariatur. Excepteur sint occaecat cupidatat non proident, sunt in culpa qui officia deserunt mollit anim id est laborum.</p>
  <p>Lorem ipsum dolor sit amet, consectetur adipiscing elit, sed do eiusmod tempor incididunt ut labore et dolore magna aliqua. Ut enim ad minim veniam, quis nostrud exercitation ullamco laboris nisi ut aliquip ex ea commodo consequat. Duis aute irure dolor in reprehenderit in voluptate velit esse cillum dolore eu fugiat nulla pariatur.</p>
  <p>Lorem ipsum dolor sit amet, consectetur adipiscing elit, sed do eiusmod tempor incididunt ut labore et dolore magna aliqua. Ut enim ad minim veniam, quis nostrud exercitation ullamco laboris nisi ut aliquip ex ea commodo consequat. Duis aute irure dolor in reprehenderit in voluptate velit esse cillum dolore eu fugiat nulla pariatur. Excepteur sint occaecat cupidatat non proident, sunt in culpa qui officia deserunt mollit anim id est laborum.</p>
  <p>Lorem ipsum dolor sit amet, consectetur adipiscing elit, sed do eiusmod tempor incididunt ut labore et dolore magna aliqua. Ut enim ad minim veniam, quis nostrud exercitation ullamco laboris nisi ut aliquip ex ea commodo consequat. Duis aute irure dolor in reprehenderit in voluptate velit esse cillum dolore eu fugiat nulla pariatur.</p>
  <p>Lorem ipsum dolor sit amet, consectetur adipiscing elit, sed do eiusmod tempor incididunt ut labore et dolore magna aliqua. Ut enim ad minim veniam, quis nostrud exercitation ullamco laboris nisi ut aliquip ex ea commodo consequat. Duis aute irure dolor in reprehenderit in voluptate velit esse cillum dolore eu fugiat nulla pariatur. Excepteur sint occaecat cupidatat non proident, sunt in culpa qui officia deserunt mollit anim id est laborum.</p>
  <p>Lorem ipsum dolor sit amet, consectetur adipiscing elit, sed do eiusmod tempor incididunt ut labore et dolore magna aliqua. Ut enim ad minim veniam, quis nostrud exercitation ullamco laboris nisi ut aliquip ex ea commodo consequat. Duis aute irure dolor in reprehenderit in voluptate velit esse cillum dolore eu fugiat nulla pariatur.</p>
</div>

<!-- contact -->
<div class="marble" role="img" aria-label="Soft white marble texture background"></div>
<svg class="abs" style="left:0;top:1970px" width="1200" height="230" viewBox="0 1970 1200 230">
  <defs>
    <linearGradient id="vee2" x1="0" x2="1">
      <stop offset="0" stop-color="#0b3f7a"/><stop offset="1" stop-color="#35b3d8"/>
    </linearGradient>
  </defs>
  <path d="M0 1970 L1200 1970 L1200 1996 L400 2168 L0 1990Z" fill="#fff"/>
  <path d="M158 2055 L400 2187 L880 2064 L400 2160Z" fill="url(#vee2)"/>
</svg>

<h2 class="section-title contact-title">GET IN <span>TOUCH</span></h2>
<div class="field" style="left:165px;top:2337px;width:283px;height:48px">Full Name</div>
<div class="field" style="left:459px;top:2337px;width:282px;height:48px">Phone</div>
<div class="field" style="left:752px;top:2337px;width:283px;height:48px">Email Address</div>
<div class="field" style="left:165px;top:2397px;width:870px;height:94px">Message</div>
<a class="btn btn-send">Send Message</a>

<!-- footer -->
<svg class="abs" style="left:0;top:2550px" width="1200" height="576" viewBox="0 2550 1200 576">
  <defs>
    <linearGradient id="foot" x1="0" y1="0" x2="1" y2="0.2">
      <stop offset="0" stop-color="#0b2f66"/><stop offset="0.45" stop-color="#1c77a8"/><stop offset="1" stop-color="#3fd4ea"/>
    </linearGradient>
  </defs>
  <path d="M0 2554 L412 2643 L0 2791Z" fill="#c4c4c4"/>
  <path d="M0 2791 L412 2643 L1200 2809 L1200 3126 L0 3126Z" fill="url(#foot)"/>
</svg>

<div class="footer-brand">Pinewell Enterprise Forge</div>

<div class="col-rule" style="left:328px"></div><div class="col-line" style="left:328px"></div>
<div class="col-rule" style="left:524px"></div><div class="col-line" style="left:524px"></div>
<div class="col-rule" style="left:782px"></div><div class="col-line" style="left:782px"></div>

<h3 class="col-title" style="left:368px">Quick Links</h3>
<ul class="quick-links">
  <li><svg width="14" height="12" viewBox="0 0 14 12"><rect x="1" y="2" width="9" height="9" rx="1.5" fill="none" stroke="#fff" stroke-width="1.4"/><path d="M3.5 6l2.5 2.5L13 1.5" fill="none" stroke="#fff" stroke-width="1.6"/></svg>Home</li>
  <li><svg width="14" height="12" viewBox="0 0 14 12"><rect x="1" y="2" width="9" height="9" rx="1.5" fill="none" stroke="#fff" stroke-width="1.4"/><path d="M3.5 6l2.5 2.5L13 1.5" fill="none" stroke="#fff" stroke-width="1.6"/></svg>About Us</li>
  <li><svg width="14" height="12" viewBox="0 0 14 12"><rect x="1" y="2" width="9" height="9" rx="1.5" fill="none" stroke="#fff" stroke-width="1.4"/><path d="M3.5 6l2.5 2.5L13 1.5" fill="none" stroke="#fff" stroke-width="1.6"/></svg>Our Services</li>
  <li><svg width="14" height="12" viewBox="0 0 14 12"><rect x="1" y="2" width="9" height="9" rx="1.5" fill="none" stroke="#fff" stroke-width="1.4"/><path d="M3.5 6l2.5 2.5L13 1.5" fill="none" stroke="#fff" stroke-width="1.6"/></svg>Our Process</li>
  <li><svg width="14" height="12" viewBox="0 0 14 12"><rect x="1" y="2" width="9" height="9" rx="1.5" fill="none" stroke="#fff" stroke-width="1.4"/><path d="M3.5 6l2.5 2.5L13 1.5" fill="none" stroke="#fff" stroke-width="1.6"/></svg>Blog</li>
  <li><svg width="14" height="12" viewBox="0 0 14 12"><rect x="1" y="2" width="9" height="9" rx="1.5" fill="none" stroke="#fff" stroke-width="1.4"/><path d="M3.5 6l2.5 2.5L13 1.5" fill="none" stroke="#fff" stroke-width="1.6"/></svg>Contact Us</li>
</ul>

<h3 class="col-title" style="left:548px">Contact Info</h3>
<div class="info-item" style="top:2851px">
  <svg width="10" height="14" viewBox="0 0 10 14"><path d="M5 0a5 5 0 0 0-5 5c0 3.5 5 9 5 9s5-5.5 5-9a5 5 0 0 0-5-5zm0 7a2 2 0 1 1 0-4 2 2 0 0 1 0 4z" fill="#fff"/></svg>
  <h4>ADDRESS:</h4>
  <p>465, Lorum Ipsum Dolore Sed, Africa</p>
</div>
<div class="info-item" style="top:2928px">
  <svg width="13" height="13" viewBox="0 0 13 13"><path d="M3 0l2 3-1.3 1.6a8 8 0 0 0 4.7 4.7L10 8l3 2-1.2 2.5C6 13 0 7 .5 1.2z" fill="#fff"/></svg>
  <h4>PHONE:</h4>
  <p>+1 (888) 888 8888</p>
</div>
<div class="info-item" style="top:2988px">
  <svg width="14" height="11" viewBox="0 0 14 11"><path d="M0 0h14v1.5L7 6 0 1.5zM0 3.3l7 4.4 7-4.4V11H0z" fill="#fff"/></svg>
  <h4>EMAIL:</h4>
  <p>info@PEF.com</p>
</div>

<h3 class="col-title" style="left:808px">Sign Up To Our Newsletter</h3>
<div class="news-input">Email Address
  <svg class="abs" style="right:16px;top:17px" width="17" height="15" viewBox="0 0 17 15"><path d="M0 7L17 0 13 15 8.5 10.5 14 3 6.5 9z" fill="#2aa8d4"/></svg>
</div>
<span class="social" style="left:808px;background:#fff" role="img" aria-label="Social profile link"></span>
<span class="social" style="left:852px" role="img" aria-label="Social profile link"></span>
<span class="social" style="left:895px" role="img" aria-label="Social profile link"></span>

<div class="footer-rule"></div>
<div class="copyright">© 2024 <b>PEF</b> &nbsp; | &nbsp; All Rights Reserved</div>

</body>
</html>
```